High quality childcare centre needs a roadside banner

We need a banner designed that advertises our achievement of being rated Exceeding National Quality Standard. Which is the highest rating you can be award as part of the assessment and rating process.

Attached pdf is purely an example although the text as it stands needs to be incorporated.

Please see below for the corporate colors:

Magenta
C-0 M-100 Y-33 K-10
bf00bf

Green
C-78 M-0 Y-100 K-0
00bf00

Target Market(s)

Parents of young children that need childcare

Industry/Entity Type

Childcare

Font styles to use
Sans Serif

Requirements
Must have
• As it is a roadside banner the text should be big, bold and easy to read therefore do not use serif fonts
• Please change found to find
• Logo - see attached
• Supplied wording - see attached
• The specs for the banner are 4m x 1.25m or 4000mm x 1250mm
• The files need to be in the following format:
• jpg, eps and ai.
• Bleeds if relevant
Nice to have
• Other marketing road signs incorporate the attached 'grobold' font
• We also have a motto - 'out of little things, big things grow'
Should not have
• Serif fonts

```html
<!DOCTYPE html>
<html lang="en">
<head>
<meta charset="utf-8">
<title>Bright Sprouts – Roadside Banner</title>
<link rel="stylesheet" href="https://fonts.googleapis.com/css2?family=Luckiest+Guy&family=Nunito:wght@700&display=swap">
<style>
  :root {
    --page-bg: #bdbdbd;
    --magenta: #b800bc;
    --magenta-deep: #87008c;
    --text-shadow: #6a006e;
    --green: #00bf00;
    --white: #ffffff;
    --label: #b800bc;
  }
  html, body {
    margin: 0;
    padding: 0;
    width: 1200px;
    height: 600px;
    overflow: hidden;
    background: var(--page-bg);
  }
  .artboard {
    position: relative;
    width: 1200px;
    height: 600px;
  }
  .size-label {
    position: absolute;
    left: 100px;
    top: 114px;
    font-family: "Nunito", Arial, sans-serif;
    font-weight: 700;
    font-size: 11px;
    letter-spacing: 0.5px;
    color: var(--label);
  }
  .banner {
    position: absolute;
    left: 100px;
    top: 143px;
    width: 1000px;
    height: 313px;
    background: var(--magenta);
    overflow: hidden;
    box-shadow: 0 1px 4px rgba(0,0,0,0.25);
  }
  .badge {
    position: absolute;
    left: 0;
    top: 0;
  }
  .headline {
    position: absolute;
    left: 0;
    top: 0;
    font-family: "Luckiest Guy", "Arial Black", sans-serif;
    color: var(--white);
    text-shadow: 3px 3px 0 var(--text-shadow);
    line-height: 1;
    white-space: nowrap;
    transform-origin: left bottom;
    transform: rotate(-4deg);
  }
  .headline--intro { left: 65px; top: 64px; font-size: 22px; }
  .headline--rating-1 { left: 74px; top: 88px; font-size: 54px; }
  .headline--rating-2 { left: 78px; top: 143px; font-size: 54px; }
  .headline--invite { left: 202px; top: 190px; font-size: 22px; }
  .motto {
    position: absolute;
    left: 150px;
    top: 259px;
    font-family: "Luckiest Guy", "Arial Black", sans-serif;
    font-size: 21px;
    color: var(--white);
    text-shadow: 2px 2px 0 var(--text-shadow);
    white-space: nowrap;
  }
  .brand {
    position: absolute;
    left: 745px;
    top: 130px;
    width: 260px;
    text-align: center;
  }
  .brand__dot {
    display: block;
    width: 64px;
    height: 64px;
    margin: 0 auto 14px;
    border-radius: 50%;
    background: var(--magenta);
  }
  .brand__name {
    display: block;
    font-family: "Luckiest Guy", "Arial Black", sans-serif;
    font-size: 30px;
    color: var(--green);
    line-height: 1;
  }
  .brand__tagline {
    display: block;
    margin-top: 8px;
    font-family: "Nunito", Arial, sans-serif;
    font-weight: 700;
    font-size: 11px;
    color: var(--green);
  }
</style>
</head>
<body>
  <div class="artboard">
    <div class="size-label">Size :&nbsp; 4000mm x 1250mm</div>

    <div class="banner">
      <svg class="badge" width="1000" height="313" viewBox="0 0 1000 313" aria-hidden="true">
        <circle cx="950" cy="327" r="246" fill="var(--magenta-deep)"/>
        <circle cx="960" cy="327" r="242" fill="var(--green)"/>
        <circle cx="960" cy="327" r="229" fill="var(--white)"/>
      </svg>

      <div class="headline headline--intro">This service is rated</div>
      <div class="headline headline--rating-1">‘Exceeding National</div>
      <div class="headline headline--rating-2">Quality Standard’</div>
      <div class="headline headline--invite">Come in and find out why……</div>

      <div class="motto">Out of little things, big things grow !</div>

      <div class="brand">
        <span class="brand__dot"></span>
        <span class="brand__name">Bright Sprouts</span>
        <span class="brand__tagline">Early Development &amp; Education Centre</span>
      </div>
    </div>
  </div>
</body>
</html>
```